依頼詳細
学習塾の看板デザインをお願いします。
基板となるイメージはできていますので、
それをブラッシュアップしてもらいたいです。
写真が二種類あり、同じデザインで、写真を差し替えたバージョンを作ってください。
記載項目
会社名等 添付ファイル参照
サイズ 横1000縦1500
希望イメージ
シンプル 複雑
単色 カラフル
暗い 明るい
日常 高級
遊び心 厳粛
未来的 伝統的
女性的 男性的
希望する色
青系、水色系
納品ファイル
• イラストレーター形式 (.ai)
補足説明
ポイント

①習慣は才能を超える、というキャッチフレーズを中心に、スタイリッシュでおしゃれなんだけど、情熱が伝わってくるデザインに仕上げて欲しい。情熱は、細部へのこだわりで伝わってくるものと思っています。

②勉強は、将来のために、今できることを毎日コツコツ積み上げていく作業。
「習慣は才能を超える」という言葉は、それを実行していくためのマインドセット。
フリータイム個別指導というのは、それを支えるための仕組み。
一般の個別指導では、時間が限られていて、本人任せの部分が大きく、サポートしきれない。
ふゆもりは、それぞれの都合に合わせていつでも毎日でも通える。
小中高一貫指導で、やる気さえあれば、どこまでもフォローできるオンリーワンの塾。
そのことを、言葉ではなく、デザインで伝えられる看板にしたい。

③原案には、上記のような思いを込めているが、自分で表現できるものには限界を感じている。
プロの手を借りて、一歩先の、情熱のこもったデザインをお願いします。
追記
・シンプルだけど、細部にこだわり、丁寧に作りこまれているものを希望します。
設置場所の写真を添付しました。
これまでのご提案を見て

シンプルなもの2点
どちらかが良いなと考えています

これからご提案頂く方へ

よりシンプル、かつ
素人では作れない
他との差別化ができているデザイン
を希望します。
■ 選んだ理由

他との違いが明確だった。
自分では全くおもいつかないデザインだった。

■ 提案者全員のお礼・コメント

この度は、ご提案と修正等の迅速な対応、誠にありがとうございました。
デザインには大変満足しております。
また、何かあった時には、お願いしたいと思っています。

```html
<!DOCTYPE html>
<html lang="ja">
<head>
<meta charset="UTF-8">
<title>学習塾ふゆもり 看板</title>
<link href="https://fonts.googleapis.com/css2?family=Noto+Sans+JP:wght@400;500;700&family=Noto+Serif+JP:wght@700;900&family=Cormorant+Garamond:wght@600&display=swap" rel="stylesheet">
<style>
  :root {
    --sky-deep: #0f4fb3;
    --sky-mid: #2c86e6;
    --sky-light: #8fd0ff;
    --glow: #d8f2ff;
    --accent: #f5a623;
    --white: #ffffff;
    --ink: #2a3a52;
    --navy: #1d3f73;
    --photo-dark: #2b2f38;
    --photo-light: #c9c3bb;
  }
  * { margin: 0; padding: 0; box-sizing: border-box; }
  html, body { width: 799px; height: 1200px; overflow: hidden; background: var(--white); }
  body { font-family: "Noto Sans JP", sans-serif; }

  .signboard { position: relative; width: 799px; height: 1200px; background: var(--white); overflow: hidden; }

  .hero-visual {
    position: absolute; left: 0; top: 0; width: 799px; height: 827px;
    background:
      radial-gradient(circle at 66% 30%, var(--glow) 0%, rgba(143,208,255,0.75) 14%, rgba(44,134,230,0) 42%),
      linear-gradient(180deg, var(--sky-mid) 0%, #1f6fd6 45%, var(--sky-deep) 100%);
  }

  .catchphrase {
    position: absolute; left: 38px; top: 36px;
    font-family: "Noto Sans JP", sans-serif; font-weight: 500;
    font-size: 118px; line-height: 122px; letter-spacing: 2px;
    color: var(--white);
  }
  .catchphrase .accent { color: var(--accent); }

  .feature-box {
    position: absolute; left: 28px; top: 505px; width: 358px; height: 192px;
    border: 3px solid var(--white); border-radius: 14px;
    color: var(--white); text-align: center;
  }
  .feature-box svg { position: absolute; left: 140px; top: -30px; }
  .feature-box .pen-bg { position: absolute; left: 126px; top: -18px; width: 100px; height: 30px; background: #1d63c9; }
  .feature-box .line1 { position: absolute; top: 74px; width: 100%; font-size: 44px; font-weight: 500; letter-spacing: 2px; }
  .feature-box .line2 { position: absolute; top: 122px; width: 100%; font-size: 50px; font-weight: 500; letter-spacing: 4px; }

  .classroom-photo {
    position: absolute; left: 395px; top: 507px; width: 378px; height: 293px;
    background: linear-gradient(120deg, var(--photo-light) 0%, #9a958f 40%, var(--photo-dark) 75%, #1c1f26 100%);
  }

  .grade-span {
    position: absolute; left: 46px; top: 708px;
    font-family: "Noto Serif JP", serif; font-weight: 900;
    font-size: 50px; letter-spacing: 6px; color: var(--white);
  }
  .grade-rule { position: absolute; left: 46px; top: 772px; width: 300px; height: 2px; background: var(--white); }
  .districts {
    position: absolute; left: 46px; top: 776px;
    font-size: 30px; font-weight: 700; letter-spacing: 2px; color: var(--white);
  }

  .brand { position: absolute; left: 0; top: 850px; width: 799px; text-align: center; color: var(--navy); }
  .brand .mark { display: block; margin: 0 auto; width: 108px; height: 108px; border: 4px solid var(--navy); }
  .brand .motto { margin-top: 40px; font-size: 14px; letter-spacing: 2px; color: var(--ink); }
  .brand .name-latin { margin-top: 2px; font-size: 40px; font-weight: 500; letter-spacing: 3px; line-height: 44px; }
  .brand .name-ja { margin-top: 6px; font-size: 22px; font-weight: 500; letter-spacing: 4px; }

  .contact {
    position: absolute; left: 0; top: 1146px; width: 799px;
    display: flex; justify-content: center; gap: 30px;
    font-size: 30px; font-weight: 500; color: var(--ink);
  }
  .contact span { display: flex; align-items: center; gap: 6px; }
</style>
</head>
<body>
<div class="signboard">
  <div class="hero-visual" role="img" aria-label="青い光の中に浮かぶ横顔のシルエットと歯車・時計の抽象的なイメージ"></div>

  <h1 class="catchphrase">
    <span class="accent">習慣</span>は<br>
    <span class="accent">才能</span>を<br>
    <span class="accent">超</span>える
  </h1>

  <div class="feature-box">
    <div class="pen-bg"></div>
    <svg width="80" height="90" viewBox="0 0 80 90" aria-hidden="true">
      <g fill="none" stroke="#ffffff" stroke-width="3" stroke-linejoin="round">
        <path d="M52 6 L66 18 L30 62 L16 68 L20 52 Z"/>
        <path d="M46 14 L60 26"/>
        <path d="M10 80 C 24 70, 30 84, 44 76 S 64 78, 70 74"/>
      </g>
    </svg>
    <div class="line1">フリータイム</div>
    <div class="line2">個別指導</div>
  </div>

  <div class="classroom-photo" role="img" aria-label="教室で机に向かい勉強する制服姿の生徒たちの写真"></div>

  <div class="grade-span">小中高一貫</div>
  <div class="grade-rule"></div>
  <div class="districts">青葉／若松／緑丘</div>

  <div class="brand">
    <span class="mark"></span>
    <p class="motto">習慣は才能を超える</p>
    <p class="name-latin">FUYUMORI</p>
    <p class="name-ja">学習塾ふゆもり</p>
  </div>

  <div class="contact">
    <span>
      <svg width="28" height="28" viewBox="0 0 24 24" aria-hidden="true"><circle cx="12" cy="12" r="12" fill="#f5a623"/><path d="M8 6 L10 6 L11 9 L9.5 10.5 C10.3 12 11.7 13.5 13.5 14.5 L15 13 L18 14 L18 16 C18 17 17 18 16 18 C10 17.5 6.5 14 6 8 C6 7 7 6 8 6 Z" fill="#fff"/></svg>
      052-418-2730
    </span>
    <span>
      <svg width="26" height="30" viewBox="0 0 22 26" aria-hidden="true"><path d="M11 0 C5 0 1 4.5 1 10 C1 17 11 26 11 26 C11 26 21 17 21 10 C21 4.5 17 0 11 0 Z" fill="#f5a623"/><circle cx="11" cy="10" r="4" fill="#fff"/></svg>
      桜坂駅3番出口すぐ
    </span>
  </div>
</div>
</body>
</html>
```